Welding company needs a business card

We are looking for a logo and business card.

Contact Information for Business Card

418 Bramblecrest Lane
Harlow Falls, PA 17888
555-284-0173
Kvmetalcraft@forgepostbox.net

```html
<!DOCTYPE html>
<html lang="en">
<head>
<meta charset="utf-8">
<title>KV Metalcraft — Business Card</title>
<link href="https://fonts.googleapis.com/css2?family=Open+Sans:wght@400;600&display=swap" rel="stylesheet">
<style>
  :root {
    --backdrop: #ececee;
    --card-white: #ffffff;
    --ink: #1d1d1f;
    --flame-orange: #f47a2e;
    --flame-amber: #f5992f;
    --flame-red: #ec3a4b;
    --edge-red: #b3241a;
  }
  * { margin: 0; padding: 0; box-sizing: border-box; }
  html, body {
    width: 1200px;
    height: 900px;
    overflow: hidden;
    background: var(--backdrop);
    font-family: "Open Sans", Arial, sans-serif;
  }
  .sheet {
    width: 1200px;
    height: 900px;
    display: flex;
    flex-direction: column;
    align-items: center;
    justify-content: center;
    gap: 56px;
  }
  .card {
    width: 600px;
    height: 343px;
    border-radius: 4px;
    box-shadow: 0 2px 0 var(--edge-red), 0 14px 30px rgba(0,0,0,0.12);
    overflow: hidden;
    position: relative;
  }
  .card-front {
    background: var(--card-white);
    display: flex;
    align-items: center;
    justify-content: space-between;
    padding: 0 44px;
    gap: 32px;
  }
  .brand {
    display: flex;
    align-items: center;
    gap: 12px;
    flex: 0 0 auto;
  }
  .brand-dot {
    width: 22px;
    height: 22px;
    border-radius: 50%;
    background: var(--flame-orange);
  }
  .brand-name {
    font-weight: 600;
    font-size: 24px;
    color: var(--flame-orange);
    white-space: nowrap;
  }
  .contact {
    font-size: 16px;
    line-height: 1.35;
    color: var(--ink);
    font-style: normal;
    white-space: nowrap;
  }
  .card-back {
    background: linear-gradient(135deg, var(--flame-amber) 0%, var(--flame-orange) 45%, var(--flame-red) 100%);
    display: flex;
    align-items: center;
    justify-content: center;
  }
  .back-name {
    font-weight: 600;
    font-size: 44px;
    color: var(--card-white);
  }
</style>
</head>
<body>
  <main class="sheet">
    <section class="card card-front" aria-label="Business card front">
      <div class="brand">
        <span class="brand-dot"></span>
        <span class="brand-name">KV Metalcraft</span>
      </div>
      <address class="contact">
        418 Bramblecrest Lane<br>
        Harlow Falls, PA 17888<br>
        555-284-0173<br>
        Kvmetalcraft@forgepostbox.net
      </address>
    </section>
    <section class="card card-back" aria-label="Business card back">
      <span class="back-name">KV Metalcraft</span>
    </section>
  </main>
</body>
</html>
```